Window cleaning company in need of leaflet design

Family run business requires leaflet design.
Our company uses water fed pole with pure water which is what the leaflet needs to emphasise on (include a background picture of a water fed pole cleaning a window.)

other services we offer which i would like to include are:
• facia/soffit cleaning.
• Conservatory cleans.
• Gutter clearing which is performed by a gutter vacuum pictures of gutters before and after clean are provided to every customer if they require.
• pressure washing

uploaded company logo to be included on leaflet.
number to include is 07715264389
email address is Rtglasscare@mailbay.test
would also like a facebook symbol included to show we are on social media.
Thank you

Font styles to use
Serif
Sans Serif

Colors
00a990
33a6d7
3276b5
3277b5
34a7d8
87cfc6
33b8a4
cfdfed
85acd3

Requirements
Must have
• We use traditional and water fed pole methods of cleaning. So those hard to reach or awkward to clean windows are not a problem. No need for ladders.

Our water fed pole system uses 100% pure water. This is water that has been de-ironised and de-mineralised to ensue it’s perfectly pure for a spot free finish.

• fully insured

• regular and reliable service
• one off cleans available

Call dean on 07715264389 for a free quote

```html
<!DOCTYPE html>
<html lang="en">
<head>
<meta charset="utf-8">
<title>RT Glass Care – Leaflet</title>
<link href="https://fonts.googleapis.com/css2?family=Barlow:wght@500;600&family=Barlow+Condensed:wght@600;700&family=Barlow+Semi+Condensed:wght@600;700;800&display=swap" rel="stylesheet">
<style>
  :root {
    --navy: #27306b;
    --navy-line: #2c3577;
    --mist: #e8e9ee;
    --ink: #3d3d42;
    --charcoal: #3a3a3c;
    --white: #ffffff;
    --red: #e2232a;
    --photo-sky: #cfd3d8;
    --photo-wall: #8e9096;
  }
  * { box-sizing: border-box; margin: 0; padding: 0; }
  html, body { width: 970px; height: 1200px; overflow: hidden; background: var(--white); }
  .leaflet { position: relative; width: 970px; height: 1200px; overflow: hidden; background: var(--white); font-family: "Barlow", sans-serif; }

  .hero-photo {
    position: absolute; left: 0; top: 0; width: 970px; height: 553px;
    background: linear-gradient(160deg, var(--photo-sky) 0%, #b7bbc1 35%, var(--photo-wall) 70%, #6f6a5e 100%);
  }
  .brand-panel {
    position: absolute; left: 583px; top: 47px; width: 387px; height: 142px;
    background: var(--white); display: flex; align-items: center; justify-content: center; gap: 12px;
  }
  .brand-panel .brand-dot { width: 14px; height: 14px; border-radius: 50%; background: var(--navy); }
  .brand-name { font-family: "Barlow Semi Condensed", sans-serif; font-weight: 600; font-size: 40px; color: var(--navy); }

  .pointer { position: absolute; left: 0; top: 0; }

  .headline-band {
    position: absolute; left: 0; top: 553px; width: 970px; height: 151px; background: var(--navy);
  }
  .headline {
    position: absolute; left: 390px; top: 564px; width: 570px; text-align: center;
    font-family: "Barlow Condensed", sans-serif; font-weight: 700; font-size: 64px; line-height: 66px;
    color: var(--white); text-transform: uppercase;
  }

  .gutter-photos {
    position: absolute; left: 64px; top: 690px; width: 307px; height: 302px;
    border: 3px solid var(--navy); border-top: none; border-radius: 0 0 26px 26px; overflow: hidden; display: flex;
  }
  .gutter-photos .half { flex: 1; position: relative; }
  .gutter-photos .before { background: linear-gradient(180deg, #d9dbd6, #8f9a7a 60%, #6e7c58); }
  .gutter-photos .after { background: linear-gradient(180deg, #c9ccd0, #9aa1a8 60%, #5f6670); border-left: 1px solid #fff; }
  .tag {
    position: absolute; bottom: 38px; background: var(--red); color: var(--white);
    font-family: "Barlow Condensed", sans-serif; font-weight: 700; font-size: 18px; padding: 4px 12px;
  }
  .before .tag { left: 0; border-radius: 0 14px 14px 0; }
  .after .tag { right: 0; border-radius: 14px 0 0 14px; }

  .services-badge {
    position: absolute; left: 24px; top: 381px; width: 376px; height: 376px; border-radius: 50%;
    background: var(--mist);
  }
  .services-badge::before {
    content: ""; position: absolute; inset: 10px; border-radius: 50%; border: 1.5px dashed #8a8d99;
  }
  .service-list { position: absolute; left: 62px; top: 33px; width: 262px; list-style: none; }
  .service-list li {
    display: flex; align-items: center; justify-content: center; gap: 8px; height: 73px;
    border-bottom: 3px solid var(--navy);
    font-family: "Barlow Semi Condensed", sans-serif; font-weight: 700; font-size: 27px; line-height: 27px;
    color: var(--navy); text-transform: uppercase; text-align: center;
  }
  .service-list li:last-child { border-bottom: none; }
  .service-list svg { flex: none; }

  .intro {
    position: absolute; left: 400px; top: 742px; width: 550px; text-align: center;
    font-weight: 500; font-size: 16px; line-height: 22px; color: var(--ink);
  }
  .intro p + p { margin-top: 17px; }

  .promise-band {
    position: absolute; left: 375px; top: 910px; width: 595px; height: 68px; background: var(--navy);
    display: flex; align-items: center; justify-content: space-around; padding: 0 14px;
  }
  .promise { display: flex; align-items: center; gap: 6px; color: var(--white);
    font-family: "Barlow Semi Condensed", sans-serif; font-weight: 600; font-size: 18px; line-height: 21px; text-transform: uppercase; }

  .call-label {
    position: absolute; left: 20px; top: 1035px; width: 296px; text-align: right;
    font-family: "Barlow Semi Condensed", sans-serif; font-weight: 700; font-size: 31px; line-height: 36px;
    color: var(--ink); text-transform: uppercase;
  }
  .phone {
    position: absolute; left: 332px; top: 1012px;
    font-family: "Barlow Semi Condensed", sans-serif; font-weight: 800; font-size: 96px; line-height: 100px;
    color: var(--navy); letter-spacing: -1px;
  }

  .footer-bar { position: absolute; left: 0; top: 1129px; width: 970px; height: 71px; background: var(--charcoal); }
  .social-tab { position: absolute; left: 0; top: 1105px; }
  .social-follow {
    position: absolute; left: 30px; top: 1112px; width: 90px; text-align: center; color: var(--white);
    font-weight: 600; font-size: 13px;
  }
  .social-follow .circle { display: block; width: 46px; height: 46px; margin: 0 auto 6px; border-radius: 50%; background: var(--white); }
  .email {
    position: absolute; left: 250px; top: 1146px; width: 600px; text-align: center; color: var(--white);
    font-weight: 600; font-size: 33px; line-height: 38px;
  }
</style>
</head>
<body>
<main class="leaflet">
  <div class="hero-photo" role="img" aria-label="Photo of two window cleaners using a long water fed pole on the glass facade of a multi-storey office building"></div>

  <div class="brand-panel">
    <span class="brand-dot"></span>
    <span class="brand-name">RT Glass Care</span>
  </div>

  <svg class="pointer" width="970" height="560" viewBox="0 0 970 560">
    <polyline points="371,529 874,529 874,203" fill="none" stroke="#ffffff" stroke-width="2" stroke-dasharray="6 5"/>
    <circle cx="874" cy="203" r="5" fill="#27306b"/>
  </svg>

  <div class="headline-band"></div>
  <h1 class="headline">Water Fed Pole<br>With Pure Water</h1>

  <div class="gutter-photos">
    <div class="half before" role="img" aria-label="Gutter full of moss and debris before clearing"><span class="tag">BEFORE</span></div>
    <div class="half after" role="img" aria-label="Clean empty gutter after clearing"><span class="tag">AFTER</span></div>
  </div>

  <div class="services-badge">
    <ul class="service-list">
      <li><svg width="30" height="26" viewBox="0 0 30 26"><path d="M2 14l9 9L28 3" fill="none" stroke="#27306b" stroke-width="5"/></svg>Facia/Soffit<br>Cleaning</li>
      <li><svg width="30" height="26" viewBox="0 0 30 26"><path d="M2 14l9 9L28 3" fill="none" stroke="#27306b" stroke-width="5"/></svg>Conservatory<br>Cleans</li>
      <li><svg width="30" height="26" viewBox="0 0 30 26"><path d="M2 14l9 9L28 3" fill="none" stroke="#27306b" stroke-width="5"/></svg>Gutter<br>Clearing</li>
      <li><svg width="30" height="26" viewBox="0 0 30 26"><path d="M2 14l9 9L28 3" fill="none" stroke="#27306b" stroke-width="5"/></svg>Pressure<br>Washing</li>
    </ul>
  </div>
  <svg class="pointer" width="400" height="560" viewBox="0 0 400 560" style="top:0;left:0">
    <circle cx="371" cy="529" r="5" fill="#27306b"/>
  </svg>

  <section class="intro">
    <p>We use traditional and water fed pole methods of cleaning.<br>So those hard to reach or awkward to clean windows are not<br>a problem. No need for ladders.</p>
    <p>Our water fed pole system uses 100% pure water. This is water<br>that has been de-ironised and de-mineralised to ensue it’s<br>perfectly pure for a spot free finish.</p>
  </section>

  <div class="promise-band">
    <div class="promise"><svg width="28" height="24" viewBox="0 0 28 24"><path d="M2 13l8 8L26 3" fill="none" stroke="#fff" stroke-width="4"/></svg><span>Fully<br>Insured</span></div>
    <div class="promise"><svg width="28" height="24" viewBox="0 0 28 24"><path d="M2 13l8 8L26 3" fill="none" stroke="#fff" stroke-width="4"/></svg><span>Regular and<br>Reliable Service</span></div>
    <div class="promise"><svg width="28" height="24" viewBox="0 0 28 24"><path d="M2 13l8 8L26 3" fill="none" stroke="#fff" stroke-width="4"/></svg><span>One Off Cleans<br>Available</span></div>
  </div>

  <p class="call-label">Call Dean on<br>for a free quote</p>
  <p class="phone">07715264389</p>

  <div class="footer-bar"></div>
  <svg class="social-tab" width="300" height="95" viewBox="0 0 300 95">
    <polygon points="0,0 165,0 175,24 205,95 0,95" fill="#27306b"/>
  </svg>
  <div class="social-follow"><span class="circle"></span>FOLLOW US</div>
  <p class="email">Email: Rtglasscare@mailbay.test</p>
</main>
</body>
</html>
```